FC Varnet - Powerpoint for Sponsorship proposal

1. Introduction:
FC Varnet is seeking the development of a professional PowerPoint template to be used for club presentations, including the annual general meeting and sponsorship proposals. This template should reflect our club's identity, values, and colors, ideally incorporating the club's jersey colors.

2. Design Elements:

Color Scheme: The template should prominently feature FC Varnet's primary colors, which are red and blue, to create a strong visual association with the club.

Logo Integration: Include the club's logo in a tasteful and visible manner on each slide. The logo should be placed in a way that doesn't distract from the content but reinforces the club's identity.

Jersey Colors: If possible, incorporate the colors of the club's jerseys into the design elements or backgrounds to create a cohesive look.

3. Slide Layouts:
The template should include various slide layouts to accommodate the different sections of the presentations. Specific slide layouts should be designed for the following sections:

Title Slide: An impressive title slide with the club's logo, name, and potentially an image representing the club.

Objectives and Values: A clean and organized layout for presenting the club's objectives and core values.

Member Summary: A section for summarizing club members, categorized by type (e.g., players, coaches, volunteers).

Nationalities: A section for displaying a summary of the nationalities represented in the club.

Rankings Table: A visually appealing format for displaying league standings or rankings.

Committee Members: A slide template for introducing committee members, including their names, roles, and photos.

Financial Report: A structured layout for presenting financial data, including balance sheets and profit and loss statements.

Sponsorship Opportunities: A section for outlining the various sponsorship opportunities available, with clear details and benefits for potential sponsors.

4. Typography and Consistency:
Ensure that typography is consistent throughout the template, using easily readable fonts. Define font styles for headings, subheadings, and body text to maintain a professional look.

5. Imagery:
Incorporate high-quality images, such as action shots of matches or club events, to enhance the visual appeal of the template.

6. Simplicity and Clarity:
Maintain a clean, uncluttered design that prioritizes clarity and easy comprehension of the content. Avoid overly complex graphics or animations.

7. Customizability:
The template should be easily customizable, allowing presenters to add their content while preserving the overall design and branding.

8. Deliverables:
Provide the PowerPoint template in a format compatible with Microsoft PowerPoint.

Presentation to members or potential sponsors

Football

Sans Serif

0054AA
0677BA
7BADD7
CADEEF
E8F1F8
0094D4
00A9DD
6FCCEA
C7EBF8
E9F6FB
EB3D1F
EC4F4E
F09395
F8D3D4
FCEDEE

• See Project desscription

```html
<!DOCTYPE html>
<html lang="fr">
<head>
<meta charset="utf-8">
<title>FC Varnet – Présentation</title>
<link rel="stylesheet" href="https://fonts.googleapis.com/css2?family=Barlow+Semi+Condensed:wght@600;700&family=Barlow:wght@500&display=swap">
<style>
  :root {
    --page-bg: #e6e6e6;
    --club-blue: #0054aa;
    --deep-blue: #0a45a8;
    --stadium-blue: #1c55bd;
    --club-red: #c8001a;
    --accent-red: #d51f35;
    --white: #ffffff;
    --map-grey: #e8ecee;
    --suisse: #c7dcf8;
    --portugal: #f8c2c3;
    --france: #d8f0b4;
    --autre: #e3d8ef;
  }
  html, body {
    margin: 0;
    padding: 0;
    width: 1200px;
    height: 1200px;
    overflow: hidden;
    background: var(--page-bg);
  }
  .board {
    position: relative;
    width: 1200px;
    height: 1200px;
  }
  .slide {
    position: absolute;
    width: 889px;
    height: 500px;
    overflow: hidden;
  }
  .slide--title { left: 155px; top: 100px; }
  .slide--nationalities { left: 153px; top: 633px; }
  .slide svg { display: block; }
  .headline {
    font-family: "Barlow Semi Condensed", sans-serif;
    font-weight: 700;
  }
  .club-name {
    font-family: "Barlow Semi Condensed", sans-serif;
    font-weight: 700;
  }
  .legend-label {
    font-family: "Barlow", sans-serif;
    font-weight: 500;
    font-size: 6.5px;
    fill: var(--white);
  }
  .credit {
    font-family: "Barlow", sans-serif;
    font-size: 4px;
    fill: #001a4d;
  }
</style>
</head>
<body>
<main class="board">

  <!-- Title slide -->
  <section class="slide slide--title">
    <svg width="889" height="500" viewBox="0 0 889 500">
      <defs>
        <linearGradient id="stadiumGlow" x1="0" y1="0" x2="1" y2="1">
          <stop offset="0" stop-color="#2a5fc4"/>
          <stop offset="0.5" stop-color="#1c50b8"/>
          <stop offset="1" stop-color="#1646a8"/>
        </linearGradient>
        <linearGradient id="playerTone" x1="0" y1="0" x2="0" y2="1">
          <stop offset="0" stop-color="#d8202a"/>
          <stop offset="0.65" stop-color="#b8141e"/>
          <stop offset="1" stop-color="#1a1a1a"/>
        </linearGradient>
        <pattern id="dotGrid" width="9.5" height="9.5" patternUnits="userSpaceOnUse">
          <circle cx="1.5" cy="1.5" r="1" fill="#ffffff"/>
        </pattern>
      </defs>

      <rect class="stadium-backdrop" width="889" height="500" fill="url(#stadiumGlow)" role="img" aria-label="Photo de tribune de stade illuminée en bleu"/>

      <polygon class="red-diagonal" points="432,500 712,0 889,0 889,500" fill="var(--club-red)"/>

      <rect class="player-photo" x="590" y="0" width="299" height="500" fill="url(#playerTone)" role="img" aria-label="Photo d'un joueur en maillot rouge tenant un ballon sous le bras"/>

      <g class="club-mark">
        <circle cx="277" cy="70" r="14" fill="var(--club-red)"/>
        <text class="club-name" x="277" y="120" text-anchor="middle" font-size="28" fill="var(--white)">FC Varnet</text>
      </g>

      <g class="chevrons" fill="none" stroke="var(--white)" stroke-width="3.4" stroke-linejoin="miter">
        <polyline points="540,28 550,38.5 540,49"/>
        <polyline points="554,28 564,38.5 554,49"/>
        <polyline points="568,28 578,38.5 568,49"/>
        <polyline points="582,28 592,38.5 582,49"/>
        <polyline points="596,28 606,38.5 596,49"/>
      </g>

      <text class="headline" x="264" y="263" text-anchor="middle" font-size="72" fill="var(--white)">UN CLUB,</text>
      <text class="headline" x="264" y="340" text-anchor="middle" font-size="72" fill="var(--white)">UNE FAMILLE</text>
      <text class="headline" x="264" y="417" text-anchor="middle" font-size="72" fill="var(--accent-red)">DEPUIS 1935</text>

      <rect class="dot-grid" x="67" y="433" width="128" height="32" fill="url(#dotGrid)"/>
    </svg>
  </section>

  <!-- Nationalities slide -->
  <section class="slide slide--nationalities">
    <svg width="888" height="500" viewBox="0 0 888 500">
      <defs>
        <linearGradient id="crowdTone" x1="0" y1="0" x2="1" y2="1">
          <stop offset="0" stop-color="#1d3b6e"/>
          <stop offset="0.5" stop-color="#3b6aa8"/>
          <stop offset="1" stop-color="#1b3a70"/>
        </linearGradient>
        <pattern id="dotGridSmall" width="9.5" height="9.5" patternUnits="userSpaceOnUse">
          <circle cx="1.5" cy="1.5" r="1" fill="#ffffff"/>
        </pattern>
      </defs>

      <rect class="slide-bg" width="888" height="500" fill="var(--club-blue)"/>

      <polygon class="logo-tab" points="4,7 109,7 109,118 92,135 4,135" fill="var(--white)"/>
      <g class="club-mark">
        <circle cx="56" cy="56" r="10" fill="var(--club-red)"/>
        <text class="club-name" x="56" y="92" text-anchor="middle" font-size="19" fill="var(--club-blue)">FC Varnet</text>
      </g>

      <text class="headline" x="149" y="133" font-size="44" fill="var(--white)">NATIONALITES</text>

      <g class="chevrons" fill="none" stroke="var(--white)" stroke-width="3.2">
        <polyline points="455,108 464,118.5 455,129"/>
        <polyline points="468,108 477,118.5 468,129"/>
        <polyline points="481,108 490,118.5 481,129"/>
        <polyline points="494,108 503,118.5 494,129"/>
        <polyline points="507,108 516,118.5 507,129"/>
      </g>

      <polygon class="photo-frame" points="644,0 850,0 721,229 504,229" fill="var(--accent-red)"/>
      <polygon class="team-photo" points="650,0 840,0 717,223 516,223" fill="url(#crowdTone)" role="img" aria-label="Photo de joueurs en maillot blanc célébrant un but dans un stade"/>
      <polygon class="red-accent" points="807,17 877,17 831,97 762,97" fill="var(--accent-red)"/>
      <polygon class="red-accent-thin" points="846,0 855,0 846,16 837,16" fill="var(--accent-red)"/>

      <rect class="world-map" x="87" y="233" width="344" height="184" rx="40" fill="var(--map-grey)" opacity="0.9" role="img" aria-label="Carte du monde en gris clair"/>

      <g class="donut-chart" fill="none" stroke-width="8" transform="rotate(-90 589 335)">
        <circle cx="589" cy="335" r="56" stroke="var(--suisse)" stroke-dasharray="211.1 140.8" stroke-dashoffset="0"/>
        <circle cx="589" cy="335" r="56" stroke="var(--portugal)" stroke-dasharray="88 263.9" stroke-dashoffset="-211.1"/>
        <circle cx="589" cy="335" r="56" stroke="var(--france)" stroke-dasharray="24.6 327.3" stroke-dashoffset="-299.1"/>
        <circle cx="589" cy="335" r="56" stroke="var(--autre)" stroke-dasharray="28.2 323.7" stroke-dashoffset="-323.7"/>
      </g>
      <circle cx="589" cy="335" r="60" fill="none" stroke="#ffffff" stroke-opacity="0.25" stroke-width="0.6"/>

      <g class="chart-legend">
        <rect x="675" y="279" width="3.5" height="3.5" fill="var(--suisse)"/>
        <text class="legend-label" x="681" y="283">SUISSE</text>
        <rect x="675" y="307" width="3.5" height="3.5" fill="var(--portugal)"/>
        <text class="legend-label" x="681" y="311">PORTUGAL</text>
        <rect x="675" y="335" width="3.5" height="3.5" fill="var(--france)"/>
        <text class="legend-label" x="681" y="339">FRANCE</text>
        <rect x="675" y="363" width="3.5" height="3.5" fill="var(--autre)"/>
        <text class="legend-label" x="681" y="367">AUTRE</text>
      </g>

      <rect class="dot-grid" x="737" y="438" width="125" height="32" fill="url(#dotGridSmall)"/>

      <text class="credit" x="4" y="495">Image credit and licence note placed here</text>
    </svg>
  </section>

</main>
</body>
</html>
```